Ad Creatives for linkedin ads, google ads and facebook ads in different formats

Please provide several banner ads for linkedin, google and facebook to visualise our product offerings from our product page: https://torvelworks.com/home/quillset-products/
Just use the product names without taking any further description into account. It should be easy to consume an give a high level overview.
Please have our attached styleguide in mind.
The formats should be:
______________
LinkedIn
- Vertical (1:1.91), square (1:1), horizontal (1.91:1)
__________
Google Ads
- Responsive Display Ads, Leaderboard (728x90), Large Rectangle (336x280), Medium Rectangle (300x250), Small Square (200x200)
____________
Facebook Ads
- Image (1200x628), Carousel (1080x1080), Video (1280x720)

```html
<!DOCTYPE html>
<html lang="en">
<head>
<meta charset="UTF-8">
<title>Torvel – Digital Insurance Platform</title>
<link rel="stylesheet" href="https://fonts.googleapis.com/css2?family=Archivo:wdth,wght@62..125,100..900&display=swap">
<style>
  :root {
    --navy-deep: #0f1b36;
    --navy: #10284a;
    --teal: #1b6f86;
    --teal-glow: #2aa3b8;
    --white: #ffffff;
    --orange: #f7931e;
    --orange-band: #f79d22;
    --magenta: #a01c5f;
    --green: #8bb53a;
  }
  html, body {
    margin: 0;
    padding: 0;
    width: 1200px;
    height: 1200px;
    overflow: hidden;
    background: var(--navy-deep);
  }
  .ad {
    position: relative;
    width: 1200px;
    height: 1200px;
    overflow: hidden;
    font-family: "Archivo", Arial, sans-serif;
    background:
      radial-gradient(ellipse 70% 60% at 20% 10%, #0f3350 0%, rgba(15,51,80,0) 70%),
      linear-gradient(180deg, #0b2340 0%, var(--navy-deep) 100%);
  }
  .hero-scene {
    position: absolute;
    left: 560px;
    top: 0;
    width: 640px;
    height: 1200px;
    background:
      radial-gradient(ellipse 38% 28% at 60% 52%, rgba(62,190,205,0.75) 0%, rgba(27,111,134,0.45) 45%, rgba(16,40,74,0) 100%),
      radial-gradient(ellipse 70% 45% at 70% 30%, rgba(27,111,134,0.55) 0%, rgba(16,40,74,0) 80%),
      radial-gradient(ellipse 60% 25% at 55% 88%, rgba(120,80,60,0.35) 0%, rgba(16,30,55,0) 80%);
  }
  .brand {
    position: absolute;
    left: 119px;
    top: 128px;
    display: flex;
    align-items: center;
    gap: 18px;
  }
  .brand-dot {
    width: 44px;
    height: 44px;
    border-radius: 50%;
    background: var(--orange);
  }
  .brand-name {
    color: var(--white);
    font-weight: 300;
    font-size: 62px;
    letter-spacing: 6px;
    line-height: 1;
  }
  .headline {
    position: absolute;
    left: 94px;
    top: 352px;
    margin: 0;
    font-weight: 800;
    font-size: 67px;
    line-height: 82px;
    letter-spacing: 0.5px;
  }
  .headline-lead { display: block; color: var(--white); }
  .headline-accent { display: block; color: var(--orange); }
  .band {
    position: absolute;
    left: 89px;
    height: 135px;
    display: flex;
    align-items: center;
    color: var(--white);
    font-weight: 800;
    font-stretch: 125%;
    font-size: 51px;
    letter-spacing: 1px;
  }
  .band-product {
    top: 533px;
    width: 720px;
    padding-left: 30px;
    background: linear-gradient(90deg, var(--magenta) 0%, var(--magenta) 55%, rgba(160,28,95,0.35) 85%, rgba(160,28,95,0) 100%);
  }
  .band-platform {
    top: 691px;
    width: 560px;
    padding-left: 35px;
    background: linear-gradient(90deg, var(--orange-band) 0%, var(--orange-band) 45%, rgba(247,157,34,0.4) 80%, rgba(247,157,34,0) 100%);
  }
  .cta {
    position: absolute;
    left: 81px;
    top: 941px;
    width: 629px;
    height: 132px;
    border-radius: 30px;
    background: var(--green);
    color: var(--white);
    display: flex;
    align-items: center;
    justify-content: center;
    font-weight: 800;
    font-stretch: 125%;
    font-size: 43px;
    letter-spacing: 1.5px;
    text-decoration: none;
  }
</style>
</head>
<body>
  <main class="ad">
    <div class="hero-scene" role="img" aria-label="Small figures of people sheltering under a large blue umbrella in the rain, standing on an open hand"></div>

    <div class="brand">
      <span class="brand-dot"></span>
      <span class="brand-name">TORVEL</span>
    </div>

    <h1 class="headline">
      <span class="headline-lead">THE PROVEN</span>
      <span class="headline-accent">NEXT-GENERATION</span>
    </h1>

    <div class="band band-product">DIGITAL INSURANCE</div>
    <div class="band band-platform">PLATFORM</div>

    <a class="cta" href="https://torvelworks.com/home/quillset-products/">GET FREE QUOTE</a>
  </main>
</body>
</html>
```